Business Card Design for sports performance / psychology company

You can see my website that this is based upon here:
http://www.trelvoxcoaching.co.uk

More than happy to answer any additional questions that you might have

** Happy for any images from Pixelgrove to be used. If I go with your design I will purchase the image for you to use

Target Market(s)

Football players

Industry/Entity Type

Business

Contact Information for Business Card

Name: Dewi Ansell
Title: Clinical Hypnotherapist & Strategist
Email address: dewi@trelvoxcoaching.co.uk
Tel: 07481926657

Font styles to use
Other font styles liked:
• Same font as on website. I'm not actually sure what it is

Requirements
Must have
• Tagline:
• Ability x Form = Performance
• Don't put form down to chance
Nice to have
• Happy for designers to be creative
Should not have

```html
<!DOCTYPE html>
<html lang="en">
<head>
<meta charset="utf-8">
<title>Trelvox Coaching – Business Card</title>
<link rel="stylesheet" href="https://fonts.googleapis.com/css2?family=Jost:wght@400;500;600&display=swap">
<style>
  :root {
    --stage: #000000;
    --navy: #2a2350;
    --navy-deep: #231d47;
    --mist: #e6e5ee;
    --white: #ffffff;
  }
  * { margin: 0; padding: 0; box-sizing: border-box; }
  html, body {
    width: 1200px; height: 1000px; overflow: hidden;
    background: var(--stage);
    font-family: "Jost", "Futura", sans-serif;
  }
  .card {
    position: absolute; left: 258px; width: 683px; height: 390px; overflow: hidden;
  }
  .card--front { top: 88px; }
  .card--back { top: 521px; }

  /* Front */
  .front-photo {
    position: absolute; inset: 0;
    background:
      radial-gradient(ellipse 260px 200px at 50% 58%, rgba(240,240,252,.9), rgba(240,240,252,0) 70%),
      linear-gradient(180deg, #6f6ca3 0%, #7d7ab0 45%, #a9a7d0 60%, #9e9cc9 80%, #8784bb 100%);
  }
  .brand {
    position: absolute; left: 0; right: 0; top: 244px; text-align: center;
    font-size: 49px; font-weight: 400; letter-spacing: 1px; color: var(--navy);
    line-height: 1;
  }
  .tagline {
    position: absolute; left: 0; right: 0; top: 302px;
    display: flex; align-items: center; justify-content: center; gap: 14px;
    font-size: 19px; font-weight: 500; color: var(--navy);
  }
  .tagline__rule { width: 90px; height: 2px; background: var(--navy); }

  /* Back */
  .back-face {
    position: absolute; left: 0; top: 0; width: 100%; height: 264px;
    background: radial-gradient(ellipse 360px 200px at 55% 55%, #ffffff, var(--mist) 60%, #c9c8d8 100%);
  }
  .back-rule { position: absolute; left: 0; right: 0; top: 266px; height: 2px; background: var(--navy); }
  .identity { position: absolute; left: 0; right: 0; top: 102px; text-align: center; color: var(--navy); }
  .identity__name { font-size: 52px; line-height: 1; letter-spacing: .3px; }
  .identity__first { font-weight: 600; }
  .identity__last { font-weight: 400; }
  .identity__title {
    margin-top: 2px; font-size: 17px; font-weight: 600; letter-spacing: .8px; line-height: 20px;
  }
  .contact-band {
    position: absolute; left: 0; right: 0; top: 270px; bottom: 0; background: var(--navy-deep);
    color: var(--white); font-size: 21px; font-weight: 400; letter-spacing: .5px;
  }
  .contact-row { position: absolute; left: 0; right: 0; display: flex; justify-content: center; align-items: center; gap: 16px; }
  .contact-row--top { top: 27px; }
  .contact-row--bottom { top: 71px; }
  .contact-item { display: flex; align-items: center; gap: 7px; }
  .contact-item svg { fill: var(--white); }
</style>
</head>
<body>
  <section class="card card--front">
    <div class="front-photo" role="img" aria-label="Photograph of a floodlit football pitch with a blurred stadium crowd, tinted lavender"></div>
    <div class="brand">TRELVOX COACHING</div>
    <div class="tagline">
      <span class="tagline__rule"></span>
      <span>Where Focus Shapes Every Match</span>
      <span class="tagline__rule"></span>
    </div>
  </section>

  <section class="card card--back">
    <div class="back-face"></div>
    <div class="identity">
      <div class="identity__name"><span class="identity__first">DEWI</span><span class="identity__last">ANSELL</span></div>
      <div class="identity__title">CLINICAL HYPNOTHERAPIST<br>&amp; STRATEGIST</div>
    </div>
    <div class="back-rule"></div>
    <div class="contact-band">
      <div class="contact-row contact-row--top">
        <span class="contact-item">
          <svg width="12" height="18" viewBox="0 0 12 18"><path d="M2 0h8a2 2 0 0 1 2 2v14a2 2 0 0 1-2 2H2a2 2 0 0 1-2-2V2a2 2 0 0 1 2-2zm0 2v11h8V2zm4 12.5a1 1 0 1 0 0 2 1 1 0 0 0 0-2z"/></svg>
          07 481 926 657
        </span>
        <span class="contact-item">
          <svg width="18" height="13" viewBox="0 0 18 13"><path d="M0 0h18v13H0zm2 2v.3l7 5 7-5V2zm0 2.7V11h14V4.7l-7 5z"/></svg>
          dewi@trelvoxcoaching.co.uk
        </span>
      </div>
      <div class="contact-row contact-row--bottom">
        <span class="contact-item">
          <svg width="18" height="18" viewBox="0 0 18 18"><circle cx="9" cy="9" r="9"/><path d="M5 4c2 1 1 3 3 3s1 3 3 3-1 3 1 4M12 3c-1 2 1 3 3 3" stroke="#231d47" stroke-width="1.6" fill="none"/></svg>
          www.trelvoxcoaching.co.uk
        </span>
      </div>
    </div>
  </section>
</body>
</html>
```